INNOVATION WEBSITE NEEDED: Agency from NZ needs YOU

Please see the enclosed documents for a detailed brief. It needs to be clean / simple / elegant / premium looking - that will appeal to companies that range from start-up to multi-national!
Note:
Perhaps instead of an actual shop, people can press an 'enquire now' button?

Target Market(s)

Start ups to multi-nationals

Industry/Entity Type

Marketing

Number of Pages Required

5+ page

Requirements
Must have
• Wordpress
• SEO
• Format friendly (mobile / tablet / etc)
• I have the URL: www.dr-lanternfix.com - I would like a working website. Please let me know what else you require to 'go live' with. Thanks!
Nice to have
• Please use / improve on my current ideas
• Perhaps use my logo icon (in different colours) for each 'product'?

```html
<!DOCTYPE html>
<html lang="en">
<head>
<meta charset="utf-8">
<title>Lanternfix — Innovation on a Budget</title>
<link href="https://fonts.googleapis.com/css2?family=Open+Sans:wght@300;400;600;700&display=swap" rel="stylesheet">
<style>
:root{
  --navy:#1d2163;
  --navy-dark:#161a52;
  --blue:#1ea0dc;
  --blue-soft:#3aa7d9;
  --green:#1fae4b;
  --ink:#333;
  --muted:#777;
  --line:#e2e2e2;
  --band:#f3f3f3;
  --white:#fff;
}
*{box-sizing:border-box;margin:0;padding:0}
html,body{width:1200px;height:4212px;overflow:hidden}
body{font-family:"Open Sans",Arial,sans-serif;color:var(--ink);background:var(--white);font-size:13px;line-height:1.55;position:relative}
section,header,footer,.copyright{position:absolute;left:0;width:1200px}
.art{position:absolute;border-radius:6px}
.btn{display:inline-block;background:var(--green);color:#fff;font-size:11px;font-weight:700;padding:8px 18px;letter-spacing:.5px;text-transform:uppercase}
.btn-blue{background:var(--blue)}
h2.section-title{font-weight:300;font-size:30px;color:#444;text-align:center}
p{margin-bottom:10px}
ul.ticks{list-style:none}
ul.ticks li{padding-left:16px;position:relative;margin-bottom:4px}
ul.ticks li::before{content:"";position:absolute;left:2px;top:7px;width:6px;height:6px;border-radius:50%;background:var(--blue)}

/* header */
.site-header{top:0;height:88px;background:#fff;border-bottom:1px solid var(--line)}
.brand{position:absolute;left:0;width:1200px;top:10px;display:flex;justify-content:center;align-items:center;gap:10px}
.brand-mark{width:28px;height:28px;background:var(--navy);border-radius:50%}
.brand-name{font-size:20px;font-weight:700;color:var(--navy);letter-spacing:.5px}
.main-nav{position:absolute;left:60px;top:52px;display:flex}
.main-nav a{font-size:12px;color:#444;padding:8px 18px;text-decoration:none}
.main-nav a.active{background:var(--blue);color:#fff}
.social{position:absolute;right:60px;top:54px;display:flex;gap:6px}
.social span{width:26px;height:26px;background:var(--blue)}

/* hero */
.hero{top:88px;height:352px;background:linear-gradient(#fafafa,#f0f0f0)}
.hero .arrow{position:absolute;top:150px;width:30px;height:42px;background:var(--blue)}
.hero .arrow svg{display:block;margin:13px auto}
.hero .prev{left:0}.hero .next{right:0}
.hero-text{position:absolute;left:530px;top:100px}
.hero-text h1{font-size:38px;font-weight:700;color:var(--navy);line-height:1.1}
.hero-text .lead{font-size:17px;color:#444;margin:6px 0 16px}
.hero-offer{display:flex;align-items:center;gap:20px}
.hero-offer small{font-size:12px;color:#555;line-height:1.4}
.hero-offer b{color:var(--navy)}

/* pricing */
.pricing{top:440px;height:560px;background:var(--band)}
.plans{position:absolute;left:130px;top:100px;display:flex}
.plan{width:235px;height:340px;background:#fff;border:1px solid var(--line);text-align:center;padding-top:30px}
.plan.featured{width:240px;height:390px;margin-top:-25px;border:3px solid var(--blue);padding-top:50px}
.plan h3{font-weight:400;font-size:20px;color:var(--blue-soft)}
.plan .price{font-size:30px;font-weight:700;color:#333;margin-top:6px}
.plan .per{font-size:10px;color:var(--muted);border-bottom:1px solid var(--line);padding-bottom:14px;margin:0 30px 14px}
.plan li{list-style:none;font-size:11px;color:#666;margin-bottom:6px}
.plan .btn{margin-top:22px}
.plan.more{background:#f7f7f7;padding-top:90px}
.plan.more p{font-size:11px;color:var(--muted);padding:0 34px}

/* text + art sections */
.split{height:330px}
.split .copy{position:absolute;width:520px}
.split h2{font-weight:300;font-size:26px;color:#444;margin-bottom:12px}
.split .copy p,.split .copy li{font-size:12px;color:#555}
.split .copy strong{display:block;color:#333;font-size:12px;margin-bottom:4px}
.reboot{top:1040px}
.purpose{top:1380px}
.whatwedo{top:1710px}
.howitworks{top:2050px}

/* shop */
.shop{top:2370px;height:340px;background:var(--band);border-top:1px solid var(--line);border-bottom:1px solid var(--line)}
.shop .slide{position:absolute;left:120px;top:70px;width:960px;height:240px;background:#fff}
.shop .nav-arrow{position:absolute;top:175px;width:26px;height:26px;background:#555}
.shop .nav-arrow svg{display:block;margin:8px auto}
.shop-detail{position:absolute;left:420px;top:20px;width:500px}
.shop-detail h3{font-size:22px;font-weight:400;color:var(--blue-soft)}
.shop-detail h4{font-size:14px;font-weight:600;margin-top:8px}

/* products */
.products{top:2730px;height:300px}
.product-row{position:absolute;left:110px;top:80px;display:flex;gap:40px}
.product{width:215px;text-align:center}
.product .icon{width:70px;height:70px;border-radius:50%;background:var(--blue);margin:0 auto 12px}
.product h4{font-size:14px;font-weight:400;color:#444;margin-bottom:4px}
.product p{font-size:10px;color:var(--muted);line-height:1.5}

/* contact about */
.about-contact{top:3060px;height:340px;background:#fafafa;border-top:1px solid var(--line)}
.about-contact .copy{position:absolute;left:90px;top:30px;width:560px}
.about-contact h3{font-size:16px;font-weight:600;color:var(--navy);margin-bottom:8px}
.about-contact p{font-size:10.5px;color:#555;margin-bottom:6px}
.vault{position:absolute;left:860px;top:50px;width:280px}
.vault h4{font-size:14px;font-weight:600;color:var(--navy)}
.vault p{font-size:10.5px;color:#666}
.vault .field{display:block;margin-top:12px;height:28px;border:1px solid #ccc;background:#fff;font-size:10px;color:#999;padding:6px 8px;position:relative}
.vault .field span{position:absolute;right:0;top:0;width:30px;height:26px;background:var(--navy)}

/* team */
.team{top:3400px;height:430px}
.team .intro{position:absolute;left:180px;top:78px;width:840px;text-align:center;font-size:11.5px;color:#555}
.team-card{position:absolute;left:90px;top:190px;width:1020px;height:180px;border:1px solid var(--line);background:#fff}
.team-card .copy{position:absolute;left:270px;top:22px;width:700px;font-size:11px;color:#555}
.team-card a{color:var(--blue);font-size:11px;text-decoration:none}

/* footer */
.site-footer{top:3830px;height:330px;background:var(--navy)}
.site-footer h3{color:#fff;font-size:22px;font-weight:400;margin-bottom:14px}
.form{position:absolute;left:90px;top:30px;width:470px}
.form .row{display:flex;gap:10px;margin-bottom:10px}
.form .input{flex:1;height:32px;background:#fff;font-size:11px;color:#888;padding:8px}
.form .msg{height:120px;background:#fff;font-size:11px;color:#888;padding:8px;margin-bottom:12px}
.form .send{display:block;background:var(--blue);color:#fff;text-align:center;font-weight:700;font-size:12px;padding:9px}
.chat{position:absolute;left:640px;top:30px;width:470px;color:#dde;font-size:11.5px}
.chat p{color:#dde}
.chat ul{list-style:none;margin:8px 0 12px}
.chat li{display:flex;align-items:center;gap:8px;margin-bottom:4px}
.chat li svg{flex:none}
.copyright{top:4160px;height:52px;background:var(--navy-dark);color:#aab;font-size:11px;padding:18px 90px}
.to-top{position:absolute;right:40px;top:12px;width:28px;height:28px;background:#fff;border-radius:50%}
</style>
</head>
<body>

<header class="site-header">
  <div class="brand"><span class="brand-mark"></span><span class="brand-name">Lanternfix</span></div>
  <nav class="main-nav">
    <a class="active">Home</a><a>Shop</a><a>Our Purpose</a><a>What We Do</a><a>The Team</a><a>Contact</a>
  </nav>
  <div class="social"><span></span><span></span><span></span></div>
</header>

<section class="hero">
  <div class="arrow prev"><svg width="10" height="16"><path d="M8 1 2 8l6 7" stroke="#fff" stroke-width="2" fill="none"/></svg></div>
  <div class="art" role="img" aria-label="Illustration of a glowing light bulb with rays" style="left:250px;top:30px;width:250px;height:280px;background:radial-gradient(circle at 50% 40%,#f8c23a 0,#4fb3e6 45%,#f0f0f0 75%)"></div>
  <div class="hero-text">
    <h1>Have to come up</h1>
    <p class="lead">with a great idea, but have a limited budget and little time?</p>
    <div class="hero-offer"><span class="btn">Buy now</span><small><b>The 'Trailblazer'</b><br>2 Hours Brainstorming</small></div>
  </div>
  <div class="arrow next"><svg width="10" height="16"><path d="M2 1l6 7-6 7" stroke="#fff" stroke-width="2" fill="none"/></svg></div>
</section>

<section class="pricing">
  <div class="plans">
    <div class="plan"><h3>The 'Bandit'</h3><div class="price">$19</div><div class="per">Per Month</div><ul><li>3 Websites</li><li>5 GB Storage</li><li>2 Users</li></ul><span class="btn">Buy now</span></div>
    <div class="plan featured"><h3>The 'Trailblazer'</h3><div class="price">$19</div><div class="per">Per Month</div><ul><li>3 Websites</li><li>5 GB Storage</li><li>2 Users</li></ul><span class="btn">Buy now</span></div>
    <div class="plan"><h3>The 'Ninja'</h3><div class="price">$19</div><div class="per">Per Month</div><ul><li>3 Websites</li><li>5 GB Storage</li><li>2 Users</li></ul><span class="btn">Buy now</span></div>
    <div class="plan more"><h3>More Options</h3><p>Lorem ipsum dolor sit amet, consectetur adipiscing elit sed do tempor.</p><span class="btn btn-blue">Enquire</span></div>
  </div>
</section>

<section class="split reboot">
  <div class="art" role="img" aria-label="Illustration of a businessman running up a rising red arrow chart" style="left:150px;top:30px;width:340px;height:270px;background:linear-gradient(135deg,#f7f7f7,#e8eef4 60%,#f2d4d0)"></div>
  <div class="copy" style="left:600px;top:20px">
    <h2>Re-boot or Kick-start...?</h2>
    <p>Do you need to reboot or kick-start your company's innovation capabilities in terms of process, people or projects?</p>
    <strong>Do you need:</strong>
    <ul class="ticks"><li>a new way of doing something?</li><li>a brilliant breakthrough idea?</li><li>a 2-5 year roadmap of strategic innovation?</li></ul>
    <p>Or, simply a new perspective to jump-start the team? If you have answered yes to any of the above, consider innovation. We create innovation that hits the bottom line.</p>
  </div>
</section>

<section class="split purpose">
  <div class="copy" style="left:90px;top:10px;text-align:right;width:600px">
    <h2>Our Purpose</h2>
    <p>Our purpose is to re-define how companies see and gain innovation quickly. The team at the innovation lab have worked both client side and as consultants. We know what works and how things get implemented.</p>
    <p>As we can see about getting outcomes, never need to leave our strategically cultured and connected roots.</p>
    <p>We get that. We can help you achieve that. That's our purpose.</p>
  </div>
  <div class="art" role="img" aria-label="Illustration of a businessman holding a target with an arrow in the bullseye" style="left:800px;top:10px;width:250px;height:280px;background:linear-gradient(160deg,#f5f5f5,#e7e9f2 55%,#f1d5d2)"></div>
</section>

<section class="split whatwedo">
  <div class="art" role="img" aria-label="Illustration of a cheering businessman at his desk" style="left:100px;top:10px;width:320px;height:300px;background:linear-gradient(160deg,#f3f3f3,#dfe3ef 60%,#c9d2e6)"></div>
  <div class="copy" style="left:560px;top:0">
    <h2>What we do</h2>
    <p>We innovate. For you.<br>This must connect things we hear are:</p>
    <strong>Do you need:</strong>
    <ul class="ticks"><li>"I need a breakthrough innovation, but am staring at a blank piece of paper"</li><li>"I have to come up with a great idea, but have a limited budget and little time"</li><li>"It's hard to get all the different functions and people aligned, so we're getting nowhere"</li></ul>
    <p>That's where we can help. We've been there and done that, many times. What we do is:</p>
    <ul class="ticks"><li>Deliver big ideas</li><li>Fast and affordable</li><li>Bring it to all levels</li></ul>
  </div>
</section>

<section class="split howitworks">
  <div class="copy" style="left:90px;top:10px;width:560px;text-align:right">
    <h2>How it works</h2>
    <p>Instead of asking for a quote like with most agencies, we have a pre-set price. You can order our services online.</p>
    <p>Pick the level and timeframe with clear goals that suits your budget and needs. Simply have a look at our innovation shop and see what you need. Do what you think works best for your team.</p>
    <p>Once booked, the team will be ready to meet and workshop with you. If you need tailored innovation, simply give the team at the innovation lab a call and we can have a quick chat first.</p>
  </div>
  <div class="art" role="img" aria-label="Illustration of a relaxed businessman leaning back with a laptop" style="left:760px;top:20px;width:330px;height:260px;background:linear-gradient(160deg,#f4f4f4,#e3e7f0 60%,#d7dbe8)"></div>
</section>

<section class="shop">
  <h2 class="section-title" style="margin-top:18px">Innovation Shop</h2>
  <div class="nav-arrow" style="left:80px"><svg width="8" height="10"><path d="M6 1 2 5l4 4" stroke="#fff" stroke-width="2" fill="none"/></svg></div>
  <div class="slide">
    <div class="art" role="img" aria-label="Photo of an espresso coffee machine" style="left:40px;top:20px;width:300px;height:200px;background:linear-gradient(160deg,#fff,#d6d6d6 50%,#9a9a9a)"></div>
    <div class="shop-detail">
      <h3>The Bandit</h3>
      <h4>Cost:</h4><p>What you get</p>
      <h4>Free cup of coffee!</h4>
      <ul class="ticks" style="font-size:12px;color:#555;margin-top:6px"><li>Free 15 Minute Chat</li><li>A pointing brief &amp; feedback to your job that needs to be done</li><li>We challenge and build any ideas you already have in mind</li></ul>
    </div>
  </div>
  <div class="nav-arrow" style="right:80px"><svg width="8" height="10"><path d="M2 1l4 4-4 4" stroke="#fff" stroke-width="2" fill="none"/></svg></div>
</section>

<section class="products">
  <h2 class="section-title" style="margin-top:10px">Product Slider</h2>
  <div class="product-row">
    <div class="product"><div class="icon"></div><h4>Product 1</h4><p>Lorem ipsum dolor sit amet, consectetuer adipiscing elit. Aenean commodo ligula eget dolor aenean massa.</p></div>
    <div class="product"><div class="icon"></div><h4>Product 2</h4><p>Lorem ipsum dolor sit amet, consectetuer adipiscing elit. Aenean commodo ligula eget dolor aenean massa.</p></div>
    <div class="product"><div class="icon"></div><h4>Product 3</h4><p>Lorem ipsum dolor sit amet, consectetuer adipiscing elit. Aenean commodo ligula eget dolor aenean massa.</p></div>
    <div class="product"><div class="icon"></div><h4>Product 4</h4><p>Lorem ipsum dolor sit amet, consectetuer adipiscing elit. Aenean commodo ligula eget dolor aenean massa.</p></div>
  </div>
</section>

<section class="about-contact">
  <div class="copy">
    <h3>Contact us about:</h3>
    <ul class="ticks" style="font-size:10.5px;color:#555;margin-bottom:8px"><li>Our customised workshops</li><li>The Innovation 'Express' Support — where we work with you on your key breakthrough innovation project over time</li></ul>
    <p><b>The fine print</b></p>
    <p>Graphic design, visualisation services not included. This can be arranged for an additional fee if desired.</p>
    <p>Consumer research — both qualitative and quantitative is not included. We can arrange research partners and support in the required brief for an additional fee.</p>
    <p>Prices exclude GST, travel &amp; accommodation (where applicable). Prices valid until October 2016. We reserve the right to change pricing from this date.</p>
  </div>
  <div class="art" role="img" aria-label="Illustration of a mascot character in a top hat" style="left:740px;top:50px;width:90px;height:120px;background:linear-gradient(#2a2f7a,#4a8fd0)"></div>
  <div class="vault">
    <h4>Idea Vault</h4>
    <p>Subscribe to unlock the Ideavault — the idea vault contains ideas that might be of interest for your business.</p>
    <span class="field">Enter your email address<span></span></span>
  </div>
</section>

<section class="team">
  <h2 class="section-title" style="margin-top:20px">The Team</h2>
  <p class="intro">We are a small team driven by innovation and focused on action, leveraging an innovative approach to team set-up; we can call on a vast array of skilled team members depending on the assignment. Tapping into a worldwide network of highly skilled consultants, there is no project we can't handle.</p>
  <div class="team-card">
    <div class="art" role="img" aria-label="Portrait area for the team lead" style="left:40px;top:28px;width:190px;height:120px;background:linear-gradient(135deg,#f1f3f8,#c9d0e6)"></div>
    <div class="copy">
      <p>Sara has over 20 years of global marketing and innovation experience. She has worked client side on some of the world's most iconic brands, such as Tidemoor, Northfield, Aspenrow and Coralby and knows how to get things done internally. She has been instrumental in building some of the strongest innovation functions, working together with R&amp;D, operations, supply chain, the executive board and the C-suite.</p>
      <p>The lab's founder is one of the most creative thinkers in New Zealand and an inspirational and innovative conductor whose teams bring new ideas to life.</p>
      <a>Read more</a>
    </div>
  </div>
</section>

<footer class="site-footer">
  <div class="form">
    <h3>Contact Us</h3>
    <div class="row"><div class="input">Name*</div><div class="input">Email*</div></div>
    <div class="msg">Message</div>
    <span class="send">SEND</span>
  </div>
  <div class="chat">
    <h3>Let's have a chat</h3>
    <p>The team at the innovation lab is flexible in terms of time and location — using today's tech savvy, we can be with you virtually anywhere, anytime. If you are in Europe, we can work while you sleep!</p>
    <ul>
      <li><svg width="12" height="12"><circle cx="6" cy="6" r="5" fill="var(--blue)"/></svg>Email: hello@dr-lanternfix.com</li>
      <li><svg width="12" height="12"><path d="M3 1h2l1 3-1.5 1a7 7 0 0 0 3.5 3.5L9 7l3 1v2a2 2 0 0 1-2 2A9 9 0 0 1 1 3a2 2 0 0 1 2-2z" fill="var(--blue)"/></svg>Tel: +64 (0) 9 000 4417</li>
      <li><svg width="12" height="12"><path d="M6 0a4 4 0 0 1 4 4c0 3-4 8-4 8S2 7 2 4a4 4 0 0 1 4-4z" fill="var(--blue)"/></svg>Level 4, 18 Harbourline Lane, Auckland, New Zealand</li>
      <li><svg width="12" height="12"><circle cx="6" cy="6" r="5" fill="none" stroke="var(--blue)" stroke-width="1.5"/></svg>www.dr-lanternfix.com</li>
    </ul>
    <p>New Zealand is one of the most beautiful, creative tech spots in the world. It is an inspirational and innovative conductive locale and our offices can also be used for workshops.</p>
  </div>
</footer>
<div class="copyright">Copyright 2016 | All Rights Reserved<span class="to-top"></span></div>

</body>
</html>
```